National Human Immunology Network Needs a Brochure DesignBrochure Design Project

We need a brochure design for a new Canadian network called VEKO. VEKO stands for "VRSL Cellular Defence Alliance". (VRSL is the Northfield Councils of Medical Inquiry and is the funder of the network).

The VRSL Cellular Defence Alliance (VEKO) is a resource network that facilitates, promotes and enhances research in human immunology and its translation into clinical care and public policy. VEKO is an inclusive National Network with International projections that will act as a coordinating resource for investigators working in different aspects of Human Immunology. As a research network, VEKO will operate as a resource “umbrella” network, facilitating communication between nodes, each with their specialized expertise in human immunology,
collaboration and knowledge exchange.

We have a VEKO logo already designed as well as the text to be used in the brochure. In addition we should include the VRSL logo somewhere on the brochure, but it does need to be front and centre. Thinking that a tri-fold brochure would work best.

Target Market(s)

Researchers, politicians, lay public

Industry/Entity Type

Communication

Requirements
Must have
• Must use logo provided.

```html
<!DOCTYPE html>
<html lang="en">
<head>
<meta charset="utf-8">
<title>VRSL Cellular Defence Alliance – Brochure</title>
<link href="https://fonts.googleapis.com/css2?family=Open+Sans:wght@700;800&family=Source+Sans+3:ital,wght@0,300;1,300&display=swap" rel="stylesheet">
<style>
:root{
  --red:#b41f29;
  --ink:#3a3a3a;
  --heading:#1f1f1f;
  --muted:#8a8a8a;
  --panel:#f1f1f1;
  --panel-dark:#e2e2e2;
  --logo-grey:#555555;
  --white:#ffffff;
}
*{margin:0;padding:0;box-sizing:border-box}
html,body{width:1200px;height:927px;overflow:hidden;background:var(--white)}
body{font-family:"Source Sans 3",Arial,sans-serif;font-weight:300;color:var(--ink);position:relative}
.band{position:absolute;left:0;width:1200px;background:var(--red)}
.band--top{top:0;height:33px}
.band--bottom{top:893px;height:34px}
.page{position:absolute;top:33px;left:0;width:1200px;height:860px;
  background:linear-gradient(90deg,var(--white) 0,var(--panel) 40%,var(--panel-dark) 100%)}
.photo{position:absolute;left:0;top:0;width:400px;height:860px;
  background:linear-gradient(160deg,#cfd6dc 0%,#9aa7b3 30%,#7b6a60 55%,#c9cfd4 80%,#e9ecee 100%)}
.brand{position:absolute;display:flex;align-items:center;gap:12px}
.brand__mark{background:var(--red)}
.brand__rule{width:2px;background:var(--logo-grey);align-self:stretch}
.brand__name{font-family:"Open Sans",Arial,sans-serif;font-weight:800;color:var(--logo-grey);text-transform:uppercase}
.brand--photo{left:30px;top:740px;height:88px}
.brand--photo .brand__mark{width:72px;height:72px}
.brand--photo .brand__name{font-size:17px;line-height:21px}
.brand--panel{left:835px;top:20px;height:138px}
.brand--panel .brand__mark{width:112px;height:112px}
.brand--panel .brand__name{font-size:26px;line-height:32.5px}
h2{font-family:"Open Sans",Arial,sans-serif;font-size:16.5px;font-weight:700;color:var(--heading);line-height:20px;margin-bottom:0}
.column{position:absolute}
.column--middle{left:437px;top:27px;width:335px}
.column--right{left:833px;top:184px;width:345px}
.list{list-style:none;font-size:15px;line-height:18.2px}
.list--bullets li::before{content:"•\00a0\00a0"}
.block{margin-bottom:20px}
.accomplishments{position:absolute;left:437px;top:630px;width:335px;color:var(--muted);font-size:11.6px;line-height:14.6px}
.accomplishments h3{font-family:"Open Sans",Arial,sans-serif;font-size:11.6px;font-weight:700;color:#555;margin-bottom:3px}
.accomplishments ul{list-style:none}
.accomplishments li::before{content:"•\00a0\00a0"}
.note{position:absolute;left:833px;top:531px;font-size:11px;font-style:italic;color:var(--muted)}
.next{position:absolute;left:812px;top:557px;width:388px;height:52px;background:var(--red);color:var(--white);
  font-size:23px;line-height:52px;padding-left:22px}
.next-copy{position:absolute;left:833px;top:626px;width:330px;font-size:15px;line-height:18.2px}
</style>
</head>
<body>
<div class="band band--top"></div>
<main class="page">
  <div class="photo" role="img" aria-label="Photograph of a researcher in gloves pipetting a red sample into a tube in a laboratory"></div>
  <div class="brand brand--photo">
    <span class="brand__mark"></span><span class="brand__rule"></span>
    <span class="brand__name">VRSL<br>Cellular<br>Defence<br>Alliance</span>
  </div>

  <section class="column column--middle">
    <div class="block">
      <h2>SPECIFIC AIMS:</h2>
      <ul class="list list--bullets">
        <li>To be a source of standardized protocols for human immunology research;</li>
        <li>To facilitate access to research material and technologies, and to expedite regulatory processes;</li>
        <li>To engage national and international human immunology stakeholders to promote research in human immunology; and</li>
        <li>To lead the development of activities of knowledge dissemination in human immunology at national and international levels.</li>
      </ul>
    </div>
    <div class="block">
      <h2>DELIVERABLES:</h2>
      <ol class="list">
        <li>1.To standardize protocols for human sample processing and sharing;</li>
        <li>2.To facilitate access to research material and reagents through formalized collaborations;</li>
        <li>3.To expedite ethical and biosafety protocols for human immunology research;</li>
        <li>4.To organize an Annual International Conference on human infection and immunity;</li>
        <li>5.To provide linkage between the Canadian human immunology research community and international organization-based initiatives in human immunology research.</li>
      </ol>
    </div>
  </section>

  <section class="accomplishments">
    <h3>ACCOMPLISHMENTS:</h3>
    <p>In its first year of operation, VEKO has made significant strides in the establishment of the network. Accomplishments to date include:</p>
    <ul>
      <li>Establishment and set-up of the administrative coordinating node</li>
      <li>Launch of the VEKO website</li>
      <li>Face-to-face meeting of the node leaders in December 2011, and regular monthly teleconference meetings</li>
      <li>Organization of a satellite symposium on “Balanced Defence Pathways in Everyday Cells” at CELLMEET 2012 in Harbourton in partnership with the Northfield Immunology Society</li>
      <li>Formation of an External Advisory Board to provide advice and guidance to the network</li>
    </ul>
  </section>

  <div class="brand brand--panel">
    <span class="brand__mark"></span><span class="brand__rule"></span>
    <span class="brand__name">VRSL<br>Cellular<br>Defence<br>Alliance</span>
  </div>

  <section class="column column--right">
    <div class="block">
      <h2>STRUCTURE OF VEKO:</h2>
      <ul class="list list--bullets"><li>Director of VEKO– Lorien Castellane (Harrowgate University</li></ul>
    </div>
    <div class="block">
      <h2>NODES &amp; LEADERS:</h2>
      <ul class="list list--bullets">
        <li>Seabrook University – Miles Ardenfeld</li>
        <li>Harrowgate University – Dario Valcorte</li>
        <li>University of Lakeview – Nadia Prewitt</li>
        <li>Calder University – Owen Treloar</li>
        <li>Westmark University* – Ravindra Malhotri</li>
        <li>University of Prairiefield – Grant Holloway</li>
        <li>University of Pacific Ridge – Wei-Lin Maro</li>
      </ul>
    </div>
    <div>
      <h2>EXTERNAL ADVISORY BOARD</h2>
      <ul class="list list--bullets">
        <li>Dr. Harlan Westby</li>
        <li>Dr. Celia Brannock</li>
        <li>Dr. Morris Quillan</li>
      </ul>
    </div>
  </section>
  <p class="note">*Note that Westmark University is the administrative coordinating node for VEKO</p>

  <h2 class="next">NEXT STEPS</h2>
  <p class="next-copy">As VEKO moves forward into the second year of its mandate, plans are in the works for expansion of the network. In addition, presence at international meetings and conferences will be ramped up to increase the profile of the network. VEKO plans on organizing community events across the country to inform the public of current research in human immunology. Finally, a focus on providing resources to trainees and fellows in the form of training seminars will also be examined as a possible resource that can be provided by VEKO.</p>
</main>
<div class="band band--bottom"></div>
</body>
</html>
```